Creative Realtor Business Card Design

I need a creative business card.... I would like it to be larger than the normal size...heavy stock.... colorful...
As you are probably aware, there are tons of realtors, and most of their cards ALL look alike.. potential clients are looking for agents that are professional, but are different.
Cards are a form of advertising and I need your help to make mine stand out in a professional, classy way.
I don't need to use the harbor sage realty logo, my personal logo is MORE important for branding purposes. OR..what is your opinion?
YOU DESIGN FOR ME PLEASE! If I could do what you do I would.... I can't and I need your professional help.

                                        If you think I need the card to be double sided so it doesn't look busy by all means I will happily accept double sided. 

I am very interested in a more "creative" card than a standard run of the mill realtor card.    I care about my clients LONG after the sale has closed!

                                   

THANK YOU SO MUCH FOR YOUR EFFORTS AND TALENTS....I APPRECIATE IT SO MUCH! 

                                        Would it be possible to use my theme of my logo to design my card?

                                            Where Keys Meet Kindred Spirits

                              

 

Please make cards larger size .... See this link for ideas that appeal to me. Thank you for your interest.

https://www.lookwidely.example/find?q=examples+of+unique+business+cards&mode=img&ref=7QpL2xV9

I want my card to stand out in size and design...

Thank you so much for your hard work for me.

Lorna

 

Reason: I learned that many designers are very busy. I am providing more time and money in hopes that designers will find it an attractive enough challenge to participate. My business cards are one of my most important marketing materials...I NEED THEM TO BE DISTINCTIVE, CLASSY, and INFORMATIVE. Thank you SO MUCH....and I will be anxiously awaiting your great designs... Lorna

Hello Designers,

Thank you to all you creative people that have kindly offered to submit your creative design(s) for my business card.  I view your designs as your creative artwork. I am anxious to see where your creativity leads you.

I wanted to share with you that my logo was something I personally designed after being in business for 3  years. ( I did have to have a professionals like yourselves draw it for me). The design and logo captured perfectly how I felt about my work ...helping individuals, such as you, find a home.  A house is easy to find, but a home is a place that has "good" energy ... a place where you feel comfortable and can grow.  A place that just "Feels right!"  It's one of those things that you just KNOW when it is right! 

I hope by sharing this bit of information about me can help you creatively design my card for me...I care for my clients LONG after the transaction has closed and they are in their home. Thank you again for taking the time to work on my design. I have been adding money so that your time spent on my card is worth it.

I do need my card soon...so please, if you have a design...submit it!

Kind Regards,

Lorna

Target Market(s)

I have a variety of clients from a mobile home of $35,000 to an estate property for $5M. I feel comfortable working with all types of people...I love my job...I love helping people find the right home because we all know how our home environment affects our well being.

Industry/Entity Type

Advertising

Contact Information for Business Card

Lorna Pratley, Realtor
Harbor Sage Realty
"Where Keys Meet Kindred Spirits"
www.lornanestfinder.example
lpratley@mailbarn.example
(555) 418-2093
BRE #04872351, Exp. 8/15

Colors

Designer to choose colors to be used in the design.

Requirements
Must have
• By law, my license number information MUST be on my card.
Nice to have
• I would love card to be memorable...if that is possible for a business card. Also, I would like my card to be larger than the average card. Not sure that is possible either.

```html
<!DOCTYPE html>
<html lang="en">
<head>
<meta charset="utf-8">
<title>Lorna Pratley – Business Card</title>
<link rel="stylesheet" href="https://fonts.googleapis.com/css2?family=Cinzel:wght@600&family=Open+Sans:wght@400;700;800&family=Great+Vibes&display=swap">
<style>
  :root {
    --bg: #eeeeee;
    --card-green: #12a84e;
    --green-faint: #3fbd6f;
    --band-red: #ec1c24;
    --ink: #1b1b1b;
    --white: #ffffff;
  }
  * { margin: 0; padding: 0; box-sizing: border-box; }
  html, body { width: 1200px; height: 795px; overflow: hidden; }
  body {
    background: var(--bg);
    font-family: "Open Sans", Arial, sans-serif;
    position: relative;
  }
  .card {
    position: absolute;
    top: 250px;
    width: 500px;
    height: 290px;
    background: var(--card-green);
    box-shadow: 0 6px 18px rgba(0,0,0,.12);
    overflow: hidden;
  }
  .card--front { left: 70px; }
  .card--back { left: 630px; }

  .band {
    position: absolute;
    left: 0; right: 0; bottom: 0;
    height: 38px;
    background: var(--band-red);
    color: var(--white);
    font-size: 12px;
    font-weight: 700;
    letter-spacing: .2px;
    display: flex;
    align-items: center;
    padding-left: 70px;
  }
  .band::before {
    content: "";
    position: absolute;
    left: 0; right: 0; top: 0;
    height: 6px;
    background: var(--card-green);
    opacity: 0;
  }

  .brand {
    position: absolute;
    display: flex;
    flex-direction: column;
    align-items: center;
    gap: 8px;
  }
  .brand__tagline {
    color: var(--white);
    font-size: 9px;
    letter-spacing: .3px;
  }
  .brand__mark {
    display: flex;
    align-items: center;
    gap: 8px;
  }
  .brand__dot {
    width: 34px; height: 34px;
    border-radius: 50%;
    background: var(--band-red);
  }
  .brand__name {
    font-family: "Cinzel", Georgia, serif;
    font-weight: 600;
    font-size: 20px;
    color: var(--white);
    letter-spacing: .5px;
  }
  .card--front .brand { left: 40px; top: 50px; }
  .card--back .brand { right: 28px; top: 108px; }

  .contact {
    position: absolute;
    left: 290px;
    top: 78px;
    color: var(--ink);
    font-size: 11px;
    line-height: 1.55;
  }
  .contact__name { font-size: 14px; margin-bottom: 2px; }
  .contact__name strong { font-weight: 700; }
  .contact__gap { height: 10px; }

  .slogan {
    position: absolute;
    left: 26px;
    top: 16px;
    font-weight: 800;
    font-size: 35px;
    line-height: 38px;
    color: var(--green-faint);
    letter-spacing: -.5px;
  }
  .slogan__line { display: block; }
</style>
</head>
<body>

  <section class="card card--front" aria-label="Card front">
    <div class="brand">
      <span class="brand__tagline">Where Keys Meet Kindred Spirits</span>
      <div class="brand__mark">
        <span class="brand__dot"></span>
        <span class="brand__name">LORNA PRATLEY</span>
      </div>
    </div>

    <address class="contact" style="font-style:normal">
      <div class="contact__name">Lorna <strong>Pratley</strong></div>
      <div>Realtor</div>
      <div>Harbor Sage Realty</div>
      <div class="contact__gap"></div>
      <div>E : lpratley@mailbarn.example</div>
      <div>M : (555) 418-2093</div>
      <div class="contact__gap"></div>
      <div>#04872351, Exp. 8/15 BRE</div>
    </address>

    <div class="band">www.lornanestfinder.example</div>
  </section>

  <section class="card card--back" aria-label="Card back">
    <p class="slogan">
      <span class="slogan__line">Where Keys</span>
      <span class="slogan__line">Meet Kindred</span>
      <span class="slogan__line">Spirits</span>
    </p>

    <div class="brand">
      <span class="brand__tagline">Where Keys Meet Kindred Spirits</span>
      <div class="brand__mark">
        <span class="brand__dot"></span>
        <span class="brand__name">LORNA PRATLEY</span>
      </div>
    </div>

    <div class="band">www.lornanestfinder.example</div>
  </section>

</body>
</html>
```